Ferris Contracting LLC Business Card Design

I am looking for a creative and unique business card design. We are a commercial construction general contractor. With the name "FERRIS" Contracting, I am hoping to see some neat designs that correlate with the name.

```html
<!DOCTYPE html>
<html lang="en">
<head>
<meta charset="utf-8">
<title>Ferris Contracting LLC – Business Card</title>
<link href="https://fonts.googleapis.com/css2?family=Poppins:wght@300;400;500;700&display=swap" rel="stylesheet">
<style>
  :root{
    --backdrop:#e9e6e1;
    --blue:#2aa7dc;
    --blue-deep:#1c86c4;
    --blue-light:#3cc0ea;
    --white:#ffffff;
    --grey:#c9c9c9;
    --charcoal:#252525;
    --charcoal-soft:#323232;
    --ink-light:#e8e8e8;
  }
  *{box-sizing:border-box;margin:0;padding:0}
  html,body{width:1200px;height:780px;overflow:hidden;background:var(--backdrop)}
  body{font-family:"Poppins",sans-serif;display:flex;align-items:center;justify-content:center;gap:30px}
  .card{position:relative;width:555px;height:317px;border-radius:4px;overflow:hidden;box-shadow:0 10px 28px rgba(0,0,0,.22)}

  /* front */
  .card--front{background:linear-gradient(135deg,var(--blue-light),var(--blue-deep))}
  .card__shape{position:absolute;inset:0;width:100%;height:100%}
  .front__brand{position:absolute;left:34px;top:0;bottom:0;width:220px;display:flex;align-items:center;gap:10px}
  .brand__dot{width:26px;height:26px;border-radius:50%;background:var(--blue);flex:none}
  .front__brand .brand__name{font-weight:700;font-size:22px;line-height:1.15;letter-spacing:1px;color:var(--blue-deep)}
  .front__details{position:absolute;left:320px;top:36px;color:var(--white)}
  .person__name{font-weight:700;font-size:19px;letter-spacing:.3px}
  .person__role{font-weight:300;font-size:11px;margin-top:1px}
  .person__rule{width:120px;height:2px;background:var(--white);margin:10px 0 22px}
  .address{font-weight:400;font-size:11.5px;line-height:1.45;margin-bottom:14px}
  .contact{list-style:none;font-size:11.5px;line-height:1.5}
  .contact li{display:flex;align-items:center;gap:7px;margin-bottom:3px}
  .contact svg{width:14px;height:14px;flex:none}

  /* back */
  .card--back{background:radial-gradient(circle at 55% 40%,var(--charcoal-soft),var(--charcoal) 70%);display:flex;flex-direction:column;align-items:center;justify-content:center}
  .back__brand{display:flex;align-items:center;gap:14px}
  .back__brand .brand__dot{width:38px;height:38px}
  .back__brand .brand__name{font-weight:700;font-size:34px;letter-spacing:1px;color:var(--blue-light)}
  .back__web{position:absolute;bottom:36px;left:0;right:0;text-align:center;color:var(--ink-light);font-size:13px;letter-spacing:2px;font-weight:400}
</style>
</head>
<body>
  <section class="card card--front">
    <svg class="card__shape" viewBox="0 0 555 317" aria-hidden="true">
      <path d="M0 0 H250 Q330 150 250 317 H0 Z" fill="var(--white)"/>
      <path d="M250 0 Q330 150 250 317" fill="none" stroke="var(--grey)" stroke-width="6"/>
    </svg>
    <div class="front__brand">
      <span class="brand__dot"></span>
      <span class="brand__name">FERRIS<br>CONTRACTING</span>
    </div>
    <div class="front__details">
      <p class="person__name">DANA R COLE</p>
      <p class="person__role">CEO</p>
      <div class="person__rule"></div>
      <p class="address">4820 W. Mesa Ridge Rd.<br>Suite 210, Tempe, AZ 85281</p>
      <ul class="contact">
        <li><svg viewBox="0 0 14 14"><circle cx="7" cy="7" r="7" fill="#fff"/><path d="M4.5 3.8l1.2-.4.8 1.8-.8.6a5 5 0 0 0 2.5 2.5l.6-.8 1.8.8-.4 1.2c-3 .2-5.9-2.7-5.7-5.7z" fill="var(--blue-deep)"/></svg>(480) 555-0193</li>
        <li><svg viewBox="0 0 14 14"><circle cx="7" cy="7" r="7" fill="#fff"/><rect x="3.5" y="4.5" width="7" height="5" fill="none" stroke="var(--blue-deep)" stroke-width="1"/><path d="M3.5 4.5L7 7.3 10.5 4.5" fill="none" stroke="var(--blue-deep)" stroke-width="1"/></svg>info@ferrisbuilds.com</li>
        <li><svg viewBox="0 0 14 14"><circle cx="7" cy="7" r="7" fill="#fff"/><circle cx="7" cy="7" r="3.8" fill="none" stroke="var(--blue-deep)" stroke-width="1"/><path d="M3.2 7h7.6M7 3.2c-1.8 2-1.8 5.6 0 7.6M7 3.2c1.8 2 1.8 5.6 0 7.6" fill="none" stroke="var(--blue-deep)" stroke-width=".8"/></svg>www.ferrisbuilds.com</li>
      </ul>
    </div>
  </section>

  <section class="card card--back">
    <div class="back__brand">
      <span class="brand__dot"></span>
      <span class="brand__name">FERRIS CONTRACTING</span>
    </div>
    <p class="back__web">www.ferrisbuilds.com</p>
  </section>
</body>
</html>
```